Business Card Design Project

We have 2 businesses which help each other.

Maplewick Care (providing nurses to hospitals/nursing homes etc)

and

Maplewick HR (providing nurses to our maplewick care business - but also providing workers for farms, restaurants meatworks etc)

We would like 2 separate business cards - but similar design and feel

Target Market(s)

Managers of nursing homes, hospitals, farms, meatworks, restauants

Industry/Entity Type

Business

Requirements
Must have
• both logos
https://www.filecrate.example/s/9q2m7t4kzrx8vbn/MaplewickHR-Logo-Horizontal.ai
https://www.filecrate.example/s/kp57wx2nb8y4q1h/73918_215607_88264_sourcefile.ai

You may edit the layout of Maplewick HR logo

Name
position
mobile
Phone
name@maplewickhr.com.au
mapelwickhr.com.au

Name
position
mobile
phone
name@maplewickcare.net.au
maplewickcare.net.au

```html
<!DOCTYPE html>
<html lang="en">
<head>
<meta charset="utf-8">
<title>MaplewickHR Business Card</title>
<link rel="stylesheet" href="https://fonts.googleapis.com/css2?family=Arimo:wght@400;700&display=swap">
<style>
  :root {
    --canvas-bg: #e9eaec;
    --card-blue: #0f4f9e;
    --panel-cream: #ecebe4;
    --logo-navy: #133f7d;
    --accent-sky: #4fb3ea;
    --text-white: #ffffff;
    --divider: rgba(255, 255, 255, 0.35);
  }
  * { box-sizing: border-box; margin: 0; padding: 0; }
  html, body {
    width: 1200px;
    height: 880px;
    overflow: hidden;
    background: var(--canvas-bg);
    font-family: "Arimo", Arial, sans-serif;
  }
  .canvas {
    position: relative;
    width: 1200px;
    height: 880px;
  }
  .card {
    position: absolute;
    top: 285px;
    width: 540px;
    height: 309px;
    background: var(--card-blue);
    box-shadow: 0 6px 18px rgba(0, 0, 0, 0.18);
  }
  .card--front { left: 40px; }
  .card--back { left: 620px; }

  /* front */
  .logo-panel {
    position: absolute;
    background: var(--panel-cream);
    border-radius: 22px;
    display: flex;
    align-items: center;
  }
  .card--front .logo-panel {
    left: 100px;
    top: 48px;
    width: 340px;
    height: 150px;
    padding-left: 34px;
    gap: 16px;
  }
  .logo-mark {
    flex: none;
    border-radius: 50%;
    background: var(--card-blue);
  }
  .card--front .logo-mark { width: 46px; height: 46px; }
  .logo-name {
    color: var(--logo-navy);
    font-weight: 700;
    letter-spacing: -0.5px;
  }
  .card--front .logo-name { font-size: 38px; }
  .front-url {
    position: absolute;
    left: 0;
    right: 0;
    top: 232px;
    text-align: center;
    color: var(--text-white);
    font-size: 15px;
    letter-spacing: 3px;
  }

  /* back */
  .card--back .logo-panel {
    left: 36px;
    top: 36px;
    width: 180px;
    height: 82px;
    border-radius: 14px;
    padding-left: 14px;
    gap: 9px;
  }
  .card--back .logo-mark { width: 24px; height: 24px; }
  .card--back .logo-name { font-size: 20px; }
  .divider {
    position: absolute;
    left: 244px;
    top: 150px;
    width: 1px;
    height: 90px;
    background: var(--divider);
  }
  .contact {
    position: absolute;
    left: 262px;
    top: 150px;
    color: var(--text-white);
  }
  .contact-name {
    color: var(--accent-sky);
    font-weight: 700;
    font-size: 17px;
    letter-spacing: 0.3px;
  }
  .contact-position {
    font-size: 12px;
    margin: 2px 0 10px;
  }
  .contact-list {
    list-style: none;
    font-size: 12.5px;
    line-height: 1.35;
  }
  .contact-label {
    display: inline-block;
    width: 46px;
    color: var(--accent-sky);
    font-size: 10px;
  }
</style>
</head>
<body>
<main class="canvas">
  <section class="card card--front" aria-label="Card front">
    <div class="logo-panel">
      <span class="logo-mark"></span>
      <span class="logo-name">MaplewickHR</span>
    </div>
    <p class="front-url">www.mapelwickhr.com.au</p>
  </section>

  <section class="card card--back" aria-label="Card back">
    <div class="logo-panel">
      <span class="logo-mark"></span>
      <span class="logo-name">MaplewickHR</span>
    </div>
    <span class="divider"></span>
    <div class="contact">
      <p class="contact-name">Clara M. Whitfield</p>
      <p class="contact-position">Position</p>
      <ul class="contact-list">
        <li><span class="contact-label">mobile</span>07 5550 1846</li>
        <li><span class="contact-label">phone</span>07 5550 1846</li>
        <li><span class="contact-label">email</span>info@mapelwickhr.com.au</li>
        <li><span class="contact-label">website</span>www.mapelwickhr.com.au</li>
      </ul>
    </div>
  </section>
</main>
</body>
</html>
```